Wordpress Design Project - IT Consulting Services Web Site

Our are starting a new technology services company. We will provide services in software implementation and business intelligence.

We need a beautiful Wordpress web site design. We need a design for the homepage, and one interior content page.

The site must have a very professional and polished look and feel. What I have suggested below are things that I think work, but I am not a designer and I am open to your professional opinions. Please be willing to use your best judgment.

The homepage should have the following elements:
- A Header Area that includes:
o The company logo, and
o navigation (consistent with the interior page)
o a social media link section that includes rss feeds, youtube, facebook, linkedin and tweets
- A Body that includes:
o A slider
o An area that features up to six of the most recent or important posts including a thumbnail and small picture, a title, and a short excerpt for each.
o An area for around 100 words of text and an image
- A footer that includes:
o The company logo
o Contact information

The interior page is relatively simple. It should include the same navigation element as the homepage, and accommodate a one column text layout.

The current site …
You can visit the current site at www.plovernestworks.com I built the current site using the “Velkaro Swift Tap” premium theme. If you visit this site you get a sense of some of the things I am talking about, but there are things that I do not like about the current site. Here’s what I like and what I don’t like.

What I like about the current site:
- It is reactive – it adapts to the size of the viewing browser
- It has a “metro” feel to it. The company will have an association with Brintovax and having a “metro” theme is a plus, but not a requirement.
- It is different without being hard to navigate – the site the slider is from the “glide carousel plugin”, the posts are represented with tiles and rearrange themselves when a topic is selected.

What I don’t like:
- The site lacks a cohesive feel – it feels to me like a bunch of different elements without a single theme that pulls everything together.
- It is not aesthetically appealing to me.
- The tiles in the post section are too big.
- I don’t like the white background – I would prefer a background color and ideally a background that somehow incorporates the graphic in the logo.

About themes
As I said, I used a Velkaro theme in my design. I will be happy to continue using this theme, or would be willing to buy a new premium theme, so long as the cost is less than $100 U.S.

Site Map:
What we do
ERP Implementation
Business Intelligence
Who we are
What’s different about us
Principles
Mission, Vision, Values
Actions
How we work
What’s Different About Us
Blogs
What Papers
Presentations
Join
What we are looking for
What are you looking for?
Benefits
Context
Updates

Regarding Pictures
Please do not feel you need to use any of the pictures currently on the site.  Use whatever pictures you feel look best.  Comps are okay. 

It is not necessary to use any of the content on the current site - you do not need to use either the pictures or the text.  Please feel free to use pictures of your choice (comps okay), and/or lorem text.

The top level navigation is the navigation I would like.

Hello all,

Since this is a Wordpress project, it goes without saying I will need to implement this design in Wordpress.  It is not absolutely necessary that a design that matches an existing template (free or not), but a design that does will have an advantage over a design which requires that a new template be coded from scratch.

Thank you.

Target Market(s)

Business executives and potential employees

Industry/Entity Type

Software

Requirements
Nice to have
• It would be nice if the site was reactive.

```html
<!DOCTYPE html>
<html lang="en">
<head>
<meta charset="utf-8">
<title>Plover Nest Works — Software Implementation and Business Intelligence</title>
<link href="https://fonts.googleapis.com/css2?family=Roboto:wght@300;400;500&family=Roboto+Slab:wght@400&display=swap" rel="stylesheet">
<style>
:root{
  --brand:#1196d3;
  --brand-deep:#0a86c6;
  --ink:#2b2b2b;
  --muted:#8a8a8a;
  --navy:#0d3552;
  --page:#ececec;
  --rule:#9a9a9a;
  --white:#ffffff;
  --social:#3a6fb0;
}
*{box-sizing:border-box;margin:0;padding:0}
html,body{width:992px;height:1200px;overflow:hidden}
body{position:relative;font-family:"Roboto",Arial,sans-serif;color:var(--ink);
  background:radial-gradient(ellipse at 50% 25%,#fafafa 0%,#efefef 55%,#dedede 100%)}
.abs{position:absolute}

/* header */
.brand{left:165px;top:28px;display:flex;align-items:center;gap:8px}
.brand-name{font-size:20px;font-weight:300;color:var(--muted);letter-spacing:-.5px}
.brand-mark{width:14px;height:14px;border-radius:50%;background:var(--brand)}
.social{display:flex;gap:1px}
.social span{width:17px;height:17px;background:var(--social);display:block}
.social .alt{background:var(--brand)}
.top-social{left:756px;top:7px}
.main-nav{left:539px;top:34px;width:288px;height:32px;display:flex;border-bottom:2px solid var(--brand)}
.main-nav a{text-decoration:none;text-align:center;padding:3px 8px 0;color:var(--brand);
  border-left:1px dashed #b9d8ea;line-height:1}
.main-nav a:first-child{border-left:0}
.main-nav .label{display:block;font-size:14px;font-weight:300}
.main-nav .sub{display:block;font-size:7px;margin-top:2px}
.main-nav .active{background:#9a9a9a;color:var(--ink);width:59px}
.main-nav .active .sub{color:#eee}

/* slider */
.slide-art{left:240px;top:84px;width:512px;height:348px;
  background:linear-gradient(180deg,#f2f2f2 0%,#e4e4e4 60%,#bdbdbd 100%);border-radius:2px}
.slide-caption{left:190px;top:172px;width:409px;height:75px;background:var(--brand);
  border:1px solid #0b6fa3;color:var(--white);padding:6px 14px 0 7px}
.slide-caption .kicker{font-size:15px;font-weight:300;line-height:1}
.slide-caption .title{font-size:29px;font-weight:400;line-height:1;letter-spacing:-.5px}
.slide-caption .tail{font-size:15px;font-weight:300;text-align:right;line-height:1}
.slide-arrow{top:208px}

/* filters */
.divider{left:0;width:992px;height:1px;background:var(--rule)}
.filters{left:283px;top:445px;width:426px;height:27px;background:#f7f7f7;border:1px solid #777;
  display:flex;justify-content:center;align-items:center}
.filters a{font-size:10px;color:var(--brand);text-decoration:none;padding:0 7px;border-left:1px dashed #9cc}
.filters a:first-child{border-left:0}

/* tiles */
.tiles{left:0;top:478px;width:992px;height:288px;background:var(--brand)}
.tile{position:absolute;text-align:center;font-family:"Roboto Slab",Georgia,serif;font-size:12.5px;
  color:var(--navy);line-height:16px}
.tile svg{display:block;margin:0 auto 8px}
.vline{position:absolute;width:1px;background:#0b7fb8}
.hline{position:absolute;left:0;width:992px;height:1px;background:#0b7fb8;top:138px}

/* intro */
.band{left:0;width:992px;background:#dcdcdc}
.intro-kicker{font-size:10px;text-transform:uppercase;color:#111}
.intro-title{font-size:30px;font-weight:300;color:var(--brand);line-height:1.1;letter-spacing:-.3px}
.intro-body{font-size:11.6px;line-height:16.5px;color:#333}

/* footer */
.site-footer{left:0;top:1018px;width:992px;height:182px;background:var(--brand-deep)}
.foot-title{font-size:16px;font-weight:300;color:var(--white)}
.foot-links{list-style:none}
.foot-links li{font-size:8px;line-height:13.2px;color:#e4f3fb}
.contact li{display:flex;align-items:center;gap:4px}
.contact-with{font-size:11px;font-weight:300;color:var(--white);display:flex;align-items:center;gap:4px}
.foot-brand .brand-name{color:var(--white);font-size:17px}
.foot-brand .brand-mark{background:var(--white)}
</style>
</head>
<body>

<header>
  <div class="abs brand"><span class="brand-name">PloverNestWorks</span><span class="brand-mark"></span></div>
  <div class="abs social top-social"><span></span><span class="alt"></span><span></span><span class="alt"></span></div>
  <nav class="abs main-nav">
    <a class="active" href="#"><span class="label">What</span><span class="sub">what we do</span></a>
    <a href="#"><span class="label">Who</span><span class="sub">who we are</span></a>
    <a href="#"><span class="label">How</span><span class="sub">how we work</span></a>
    <a href="#"><span class="label">Join</span><span class="sub">join us</span></a>
    <a href="#"><span class="label">Contact</span><span class="sub">contact us</span></a>
  </nav>
</header>

<section class="slider">
  <div class="abs slide-art" role="img" aria-label="Illustration of a businessman drawing sketches of charts, devices, clouds and a city skyline on a wall"></div>
  <div class="abs slide-caption">
    <div class="kicker">Software</div>
    <div class="title">Implementation and Business</div>
    <div class="tail">Intelligence</div>
  </div>
  <svg class="abs slide-arrow" style="left:140px" width="28" height="50" viewBox="0 0 28 50"><polyline points="25,2 2,25 25,48" fill="none" stroke="#555" stroke-dasharray="1.5 1.5"/></svg>
  <svg class="abs slide-arrow" style="left:824px" width="28" height="50" viewBox="0 0 28 50"><polyline points="3,2 26,25 3,48" fill="none" stroke="#555" stroke-dasharray="1.5 1.5"/></svg>
</section>

<div class="abs divider" style="top:459px"></div>
<nav class="abs filters">
  <a href="#">All</a><a href="#">Identity</a><a href="#">People</a><a href="#">Principles</a><a href="#">Servies</a><a href="#">Thought</a><a href="#">Leadership</a><a href="#">Values</a>
</nav>

<section class="abs tiles">
  <div class="vline" style="left:307px;top:34px;height:254px"></div>
  <div class="vline" style="left:481px;top:34px;height:254px"></div>
  <div class="vline" style="left:660px;top:34px;height:254px"></div>
  <div class="hline"></div>

  <div class="tile" style="left:140px;top:34px;width:160px">
    <svg width="42" height="44" viewBox="0 0 42 44" fill="#fff"><rect x="0" y="34" width="8" height="10"/><rect x="11" y="27" width="8" height="17"/><rect x="22" y="20" width="8" height="24"/><rect x="33" y="12" width="8" height="32"/><path d="M2 28 L30 4 L26 1 L38 0 L37 12 L33 8 L6 32Z"/></svg>
    Growth is Essential</div>
  <div class="tile" style="left:314px;top:34px;width:160px">
    <svg width="44" height="38" viewBox="0 0 44 38" fill="none" stroke="#fff" stroke-width="4"><path d="M22 2 H42 V36 H22"/><path d="M0 19 H30 M20 9 L30 19 L20 29"/></svg>
    ERP implementation</div>
  <div class="tile" style="left:488px;top:34px;width:160px">
    <svg width="46" height="40" viewBox="0 0 46 40" fill="#fff"><path d="M22 12 C14 2 4 4 0 10 C8 8 14 10 20 14Z"/><path d="M24 12 C30 2 40 4 44 10 C36 8 30 10 26 14Z"/><rect x="21" y="12" width="4" height="20"/><path d="M2 40 C10 30 36 30 44 40Z"/></svg>
    Respect the journey</div>
  <div class="tile" style="left:668px;top:34px;width:180px">
    <svg width="44" height="44" viewBox="0 0 44 44"><circle cx="14" cy="14" r="10" fill="none" stroke="#fff" stroke-width="6" stroke-dasharray="4 2"/><circle cx="32" cy="32" r="8" fill="none" stroke="#fff" stroke-width="5" stroke-dasharray="3 2"/></svg>
    Experties is more useful<br>than authrity</div>

  <div class="tile" style="left:140px;top:172px;width:160px">
    <svg width="44" height="44" viewBox="0 0 44 44" fill="#fff"><rect x="2" y="0" width="18" height="44"/><rect x="22" y="14" width="20" height="30"/><g fill="#1196d3"><rect x="6" y="6" width="10" height="3"/><rect x="6" y="14" width="10" height="3"/><rect x="6" y="22" width="10" height="3"/><rect x="26" y="20" width="5" height="5"/><rect x="33" y="20" width="5" height="5"/><rect x="26" y="28" width="5" height="5"/><rect x="33" y="28" width="5" height="5"/></g></svg>
    Not like building a<br>house</div>
  <div class="tile" style="left:314px;top:172px;width:160px">
    <svg width="44" height="44" viewBox="0 0 44 44" fill="#fff"><circle cx="22" cy="20" r="10"/><rect x="17" y="30" width="10" height="8"/><rect x="19" y="40" width="6" height="3"/><g stroke="#fff" stroke-width="3"><line x1="22" y1="0" x2="22" y2="6"/><line x1="2" y1="20" x2="8" y2="20"/><line x1="36" y1="20" x2="42" y2="20"/><line x1="7" y1="6" x2="11" y2="10"/><line x1="37" y1="6" x2="33" y2="10"/></g></svg>
    What's the idea?</div>
  <div class="tile" style="left:488px;top:172px;width:160px">
    <svg width="44" height="44" viewBox="0 0 44 44"><circle cx="22" cy="22" r="18" fill="#fff"/><circle cx="18" cy="18" r="6" fill="none" stroke="#1196d3" stroke-width="3" stroke-dasharray="3 2"/><circle cx="28" cy="28" r="5" fill="none" stroke="#1196d3" stroke-width="3" stroke-dasharray="3 2"/></svg>
    Business Intelligence</div>
  <div class="tile" style="left:668px;top:172px;width:180px">
    <svg width="44" height="30" viewBox="0 0 44 30" fill="#fff"><circle cx="10" cy="10" r="5"/><circle cx="22" cy="8" r="6"/><circle cx="34" cy="10" r="5"/><path d="M2 28 C2 18 18 18 18 28Z"/><path d="M12 28 C12 14 32 14 32 28Z"/><path d="M26 28 C26 18 42 18 42 28Z"/></svg>
    People are always more<br>than labels</div>
</section>

<div class="abs band" style="top:766px;height:28px"></div>
<div class="abs divider" style="top:794px"></div>

<section>
  <div class="abs" style="left:165px;top:826px;width:290px">
    <p class="intro-kicker">People, processes and tools</p>
    <h2 class="intro-title">Putting People First</h2>
    <p class="intro-body" style="margin-top:10px">Every services firm is made up of people, processes and tools. At Plover Nest Works, we put people first, tailoring everything wedo to find, hire, train, and keep the very best people. Because once you have the best people everything else follows.</p>
  </div>
  <div class="abs" style="left:548px;top:818px;width:282px">
    <p class="intro-kicker">Plover Nest Works</p>
    <h2 class="intro-title">What's the idea?</h2>
    <p class="intro-body" style="margin-top:10px">The idea is an old one but a great one.&nbsp; Edwin Calder Rowe was an American writer credited with creating the phrase "The American Dream".&nbsp; It's the idea that your success should depend on your ability and achievements, not on where you started out.&nbsp; It's an idea we try to live up to.</p>
  </div>
</section>

<div class="abs divider" style="top:990px"></div>
<div class="abs band" style="top:991px;height:27px"></div>

<footer class="abs site-footer">
  <h3 class="abs foot-title" style="left:165px;top:18px">Site Map</h3>
  <ul class="abs foot-links" style="left:165px;top:43px">
    <li>What we do</li><li>ERP Implementation</li><li>Business Intelligence</li><li>Who we are</li><li>What's different about us</li><li>Principles</li><li>Mission, Vision, Values</li><li>Actions</li><li>How we work</li>
  </ul>
  <ul class="abs foot-links" style="left:321px;top:43px">
    <li>What's Different About Us</li><li>Blogs</li><li>What Papers</li><li>Presentations</li><li>Join</li><li>What we are looking for</li><li>What are you looking for?</li><li>Benefits</li><li>Context</li>
  </ul>
  <h3 class="abs foot-title" style="left:479px;top:18px">Contact Information</h3>
  <ul class="abs foot-links contact" style="left:479px;top:43px">
    <li><svg width="7" height="7" viewBox="0 0 10 10" fill="#fff"><path d="M2 0 L4 3 L3 4 C4 6 5 7 6 7 L7 6 L10 8 L8 10 C4 10 0 6 0 2Z"/></svg>0800-555-0142</li>
    <li><svg width="7" height="7" viewBox="0 0 10 10" fill="#fff"><rect x="1" y="0" width="8" height="10"/><rect x="3" y="2" width="4" height="2" fill="#0a86c6"/></svg>0800-555-0143</li>
    <li><svg width="7" height="7" viewBox="0 0 10 10" fill="#fff"><rect x="0" y="2" width="10" height="6"/><polyline points="0,2 5,6 10,2" fill="none" stroke="#0a86c6"/></svg>info@plovernestworks.com</li>
  </ul>
  <div class="abs contact-with" style="left:676px;top:21px">Contact with Us:
    <div class="social"><span></span><span class="alt" style="background:#5fb6e3"></span><span></span><span style="background:#5fb6e3"></span></div>
  </div>
  <div class="abs brand foot-brand" style="left:676px;top:124px"><span class="brand-name">PloverNestWorks</span><span class="brand-mark"></span></div>
</footer>

</body>
</html>
```